Fitness Body Weight Exercises Book Cover

Need a book cover design for a new book

This book is going to market to people to get in shape by playing a fitness dice game call FlexRUMBA The dice game

When people see the cover they should see that this is a book that can help them get in shape. We are positioning the guru as an expert inside of the fitness niche

Target Market(s)

fitness

Requirements
Must have
• The name of the book which is

"The Grand Victor Floorwork Regimen"

Tagline -

The Worlds #1 Resource For Combat Strength Training Using Body Weight Exercises For Men, Women and Children

__________

Featuring FlexRUMBA The Dice Game (TM)

___________________________
ON THE BACK COVER

Image with Bren with his gold medal
with these words
No Weights, No Problem

_____-

front cover
the image with him doing a push up should be on the front of the cover with these words

_________
Nice to have
• Maybe

"Bren Presents ...."

The Grand Victor Floorwork Regimen

```html
<!DOCTYPE html>
<html lang="en">
<head>
<meta charset="utf-8">
<title>The Grand Victor Floorwork Regimen — Cover Layouts</title>
<link rel="stylesheet" href="https://fonts.googleapis.com/css2?family=Anton&family=Ubuntu:wght@500;700&family=Ubuntu+Mono&family=Mr+Dafoe&family=Roboto:ital,wght@1,500&display=swap">
<style>
  :root {
    --ink: #000;
    --paper: #fff;
    --cyan: #1fd9d9;
    --cyan-soft: #2fb5b0;
    --red: #ee1c1c;
    --dark-a: #0b1211;
    --dark-b: #1f302c;
    --dark-c: #3b4a45;
    --light-a: #ffffff;
    --light-b: #e4f2f2;
    --light-c: #c9d4dc;
  }
  * { margin: 0; padding: 0; box-sizing: border-box; }
  html, body { width: 846px; height: 1200px; overflow: hidden; background: var(--paper); }
  .sheet { position: relative; width: 846px; height: 1200px; }

  .cover { position: absolute; left: 0; width: 846px; height: 570px; background: var(--ink); }
  .cover--dark { top: 0; --accent: var(--cyan); --heading: var(--paper); --body: var(--paper); }
  .cover--light { top: 630px; --accent: var(--red); --heading: var(--ink); --body: var(--ink); }

  .panel { position: absolute; top: 16px; height: 539px; overflow: hidden; }
  .cover--light .panel { top: 17px; }

  .cover--dark .panel {
    background:
      linear-gradient(115deg, transparent 0 18%, rgba(90,120,110,.18) 22%, transparent 27% 58%, rgba(70,100,92,.16) 63%, transparent 68%),
      linear-gradient(65deg, transparent 0 35%, rgba(0,0,0,.45) 45%, transparent 55% 75%, rgba(80,105,98,.2) 82%, transparent 88%),
      radial-gradient(ellipse 70% 45% at 20% 30%, rgba(74,98,90,.45), transparent 70%),
      radial-gradient(ellipse 60% 50% at 85% 80%, rgba(60,82,76,.4), transparent 70%),
      linear-gradient(170deg, var(--dark-b), var(--dark-a) 55%, var(--dark-b));
  }
  .cover--light .panel {
    background:
      linear-gradient(115deg, transparent 0 20%, rgba(170,180,205,.22) 25%, transparent 31% 62%, rgba(180,195,210,.2) 67%, transparent 72%),
      radial-gradient(ellipse 55% 35% at 30% 10%, rgba(175,185,210,.45), transparent 70%),
      radial-gradient(ellipse 60% 40% at 75% 90%, rgba(190,225,225,.55), transparent 70%),
      linear-gradient(165deg, var(--light-b), var(--light-a) 45%, var(--light-b));
  }
  .cover--dark .front {
    background:
      linear-gradient(100deg, transparent 0 30%, rgba(85,110,100,.3) 38%, transparent 46% 70%, rgba(60,80,75,.3) 78%, transparent 86%),
      radial-gradient(ellipse 80% 60% at 50% 20%, rgba(58,76,70,.55), transparent 75%),
      linear-gradient(180deg, var(--dark-b), var(--dark-a));
  }

  .back { left: 0; width: 393px; }
  .front { left: 453px; width: 393px; }

  .back__title {
    position: absolute; left: 0; width: 100%; text-align: center;
    font: 31px/1 "Anton", sans-serif; color: var(--heading); white-space: nowrap;
  }
  .cover--dark .back__title { top: 22px; }
  .cover--light .back__title { top: 44px; font-size: 33px; }

  .photo { position: absolute; }
  .photo--medal {
    background:
      linear-gradient(180deg, rgba(255,255,255,.35), transparent 25%),
      linear-gradient(90deg, #eef3ec 0%, #2f7d56 14%, #8fc7b4 24%, #b58563 36%, #c08d69 50%, #b07f5e 64%, #7fc6c3 76%, #d8efee 88%, #f7f9f9 100%);
  }
  .cover--dark .photo--medal { left: 36px; top: 73px; width: 324px; height: 304px; border: 2px solid var(--cyan); }
  .cover--light .photo--medal { left: 29px; top: 90px; width: 339px; height: 317px; border: 8px solid var(--ink); }

  .rule { position: absolute; height: 2px; background: var(--cyan); }
  .back .rule { left: 0; width: 383px; top: 485px; }
  .front .rule { left: 0; width: 100%; top: 485px; }

  .spine { position: absolute; left: 393px; top: 0; width: 60px; height: 570px; background: var(--ink); }
  .spine__title {
    position: absolute; left: 15px; top: 16px; writing-mode: vertical-rl;
    font: 20px/1 "Anton", sans-serif; color: var(--accent); white-space: nowrap; letter-spacing: -0.2px;
  }
  .spine__series {
    position: absolute; left: 10px; top: 431px; writing-mode: vertical-rl;
    font: 14px/1.3 "Anton", sans-serif; color: var(--paper); white-space: nowrap;
  }

  .front__presenter {
    position: absolute; left: 453px; top: 0; width: 393px; text-align: center;
    font: 15px/16px "Ubuntu Mono", monospace; color: var(--accent); letter-spacing: 2px;
  }
  .front__title {
    position: absolute; left: 0; width: 100%; text-align: center;
    font: 40px/1.12 "Anton", sans-serif; color: var(--heading); white-space: nowrap;
  }
  .cover--dark .front__title { top: 10px; }
  .cover--light .front__title { top: 1px; font-size: 37px; line-height: 1.1; }

  .brush { position: absolute; left: 17px; width: 362px; height: 10px; }
  .cover--dark .brush--title { top: 107px; }
  .cover--light .brush--title { top: 87px; }

  .tagline {
    position: absolute; left: 12px; width: 370px; text-align: center;
    font: 500 11.6px/22px "Ubuntu", sans-serif; color: var(--body); white-space: nowrap;
  }
  .cover--dark .tagline { top: 135px; }
  .cover--light .tagline { top: 107px; border-top: 1px solid var(--ink); border-bottom: 1px solid var(--ink); padding: 2px 0; }
  .tagline__rank { color: var(--red); font: 700 20px/1 "Ubuntu", sans-serif; }
  .tagline__rank-s { font-weight: 700; font-size: 14px; }
  .tagline__accent { color: var(--accent); }

  .photo--pushup { left: 0; width: 393px; height: 270px; }
  .cover--dark .photo--pushup {
    top: 199px;
    background:
      linear-gradient(90deg, rgba(30,34,32,.55), transparent 25% 75%, rgba(30,34,32,.35)),
      linear-gradient(180deg, #2f3533 0%, #3f4643 22%, #6a4a34 40%, #8a6247 52%, #6f4d37 64%, #6e716d 76%, #8f918c 100%);
  }
  .cover--light .photo--pushup {
    top: 170px;
    background:
      linear-gradient(90deg, rgba(60,70,68,.35), transparent 25% 75%, rgba(60,70,68,.25)),
      linear-gradient(180deg, #4d5755 0%, #66706c 22%, #8e6a50 40%, #b48463 52%, #98704f 64%, #b9bcb8 78%, #e3e5e2 100%);
  }

  .brush--shadow { left: 0; width: 393px; top: 466px; height: 16px; }
  .brush--footer { left: 0; width: 393px; top: 474px; height: 12px; }

  .featuring { position: absolute; left: 20px; white-space: nowrap; color: var(--body); }
  .cover--dark .featuring { top: 505px; }
  .cover--light .featuring { top: 499px; }
  .featuring__label { font: 30px/1 "Mr Dafoe", cursive; color: var(--accent); margin-right: 8px; }
  .featuring__game { font: italic 500 16.5px/1 "Roboto", sans-serif; }
</style>
</head>
<body>
<main class="sheet">

  <section class="cover cover--dark">
    <div class="panel back">
      <h2 class="back__title">No Weights, No Problem</h2>
      <div class="photo photo--medal" role="img" aria-label="Photo of Bren smiling, wearing his gold medal"></div>
      <div class="rule"></div>
    </div>
    <div class="spine">
      <span class="spine__title">The Grand Victor Floorwork Regimen</span>
      <span class="spine__series">flexRUMBA<br>the dice Game</span>
    </div>
    <p class="front__presenter">Bren Presents</p>
    <div class="panel front">
      <h1 class="front__title">The Grand Victor<br>Floorwork Regimen</h1>
      <svg class="brush brush--title" viewBox="0 0 362 10" preserveAspectRatio="none" aria-hidden="true">
        <rect x="0" y="0" width="362" height="1" fill="#000"/>
        <path d="M0 5 L30 3.5 L70 4.5 L120 2.8 L180 3.6 L240 2.2 L300 3 L362 2 L360 6.5 L300 7.8 L250 6.6 L190 8.6 L130 7.4 L80 9 L30 7.6 L0 8.4 Z" fill="var(--cyan-soft)"/>
      </svg>
      <p class="tagline">The Worlds <span class="tagline__rank">1#</span><span class="tagline__rank-s">S</span> Resource For Combat Strength Training<br>Using <span class="tagline__accent">Body Weight</span> Exercises For Men, Women and Children</p>
      <div class="photo photo--pushup" role="img" aria-label="Photo of Bren doing a push up on concrete"></div>
      <svg class="brush brush--shadow" viewBox="0 0 393 16" preserveAspectRatio="none" aria-hidden="true">
        <path d="M0 3 L40 5 L90 2 L150 4.5 L210 1.5 L270 4 L330 2 L393 3.5 L393 16 L0 16 Z" fill="#0d1312"/>
        <path d="M20 9 L120 8 L200 10 L300 8.5 L380 10 L380 11 L300 10 L200 11.5 L120 9.5 L20 10.5 Z" fill="#000"/>
      </svg>
      <div class="rule"></div>
      <p class="featuring"><span class="featuring__label">Featuring</span><span class="featuring__game">FlexRUMBA The Dice Game (TM)</span></p>
    </div>
  </section>

  <section class="cover cover--light">
    <div class="panel back">
      <h2 class="back__title">No Weights, No Problem</h2>
      <div class="photo photo--medal" role="img" aria-label="Photo of Bren smiling, wearing his gold medal"></div>
    </div>
    <div class="spine">
      <span class="spine__title">The Grand Victor Floorwork Regimen</span>
      <span class="spine__series">flexRUMBA<br>the dice Game</span>
    </div>
    <p class="front__presenter">Bren Presents</p>
    <div class="panel front">
      <h1 class="front__title">The Grand Victor<br>Floorwork Regimen</h1>
      <svg class="brush brush--title" viewBox="0 0 362 10" preserveAspectRatio="none" aria-hidden="true">
        <path d="M0 5 L30 3.5 L70 4.5 L120 2.8 L180 3.6 L240 2.2 L300 3 L362 2 L360 6.5 L300 7.8 L250 6.6 L190 8.6 L130 7.4 L80 9 L30 7.6 L0 8.4 Z" fill="var(--red)"/>
      </svg>
      <p class="tagline">The Worlds <span class="tagline__rank">1#</span><span class="tagline__rank-s">S</span> Resource For Combat Strength Training<br>Using <span class="tagline__accent">Body Weight</span> Exercises For Men, Women and Children</p>
      <div class="photo photo--pushup" role="img" aria-label="Photo of Bren doing a push up on concrete"></div>
      <svg class="brush brush--footer" viewBox="0 0 393 12" preserveAspectRatio="none" aria-hidden="true">
        <path d="M0 5 L50 3.5 L110 4.5 L170 2.5 L240 3.8 L310 2 L393 2.8 L393 9 L330 10.5 L260 8.6 L190 10.8 L120 9 L60 11 L0 10 Z" fill="var(--ink)"/>
      </svg>
      <p class="featuring"><span class="featuring__label">Featuring</span><span class="featuring__game">FlexRUMBA The Dice Game (TM)</span></p>
    </div>
  </section>

</main>
</body>
</html>
```